K5Lesson WebSite

an educational website about tutoring, client will be surfing this site looking for a tutor, please see the attached images because the contains exactly what we need.
Updates

Project Deadline Extended Reason: something went wrong with the uploaded files, we are very sorry.thank you PixelBazaar for the 5 days extension.now there is a 3 images describing the content of the three pages.good luck Added Friday, August 5, 2016

Target Market(s)

everyone

Industry/Entity Type

Education

Number of Pages Required

3 page

Font styles to use
Other font styles liked:
• something looks good in Arabic and english like "Droid Arabic Kufi"

Requirements
Must have
• the logo we attached, responsive design, simple, also try as much as you can Centering texts and layout because this website will have an Arabic version, Arabic is a Right-to-Left Language.
• a change language button,
Nice to have
• educational gestures.
• Centered texts and layout because this website will have an Arabic version, Arabic is a Right-to-Left Language.
• we have a web designer and we can download any template and add our logo and text to it, but.....
• we need creativity, so please stick to the contents in the images we attached, we need something very simple, more like a varnel home page with little touch of filtering fields like the 5 dropdownlist and the gender selection buttons.
• try not to go far away from the contents we specified in the images, use less images or dont use images at all, try not to make the client scroll down,
Should not have
• too much colors or noisy layout or heavy media

```html
<!DOCTYPE html>
<html lang="en">
<head>
<meta charset="utf-8">
<title>K5Lesson – Find a Tutor</title>
<link rel="stylesheet" href="https://fonts.googleapis.com/css2?family=Raleway:wght@400;500;600&family=Tinos&family=Roboto+Condensed&display=swap">
<style>
:root{
  --blue:#1e90d8;
  --blue-dark:#1565a8;
  --orange:#f26a21;
  --ink:#1a1a1a;
  --bar:#333333;
  --hero:#eef2f6;
  --field-border:#a9d3ee;
  --footer:#000000;
  --copy-bar:#3b3b3b;
  --white:#ffffff;
}
*{box-sizing:border-box;margin:0;padding:0}
html,body{width:1200px;height:1001px;overflow:hidden}
body{position:relative;background:var(--white);font-family:'Raleway',sans-serif;color:var(--ink)}
.abs{position:absolute}

/* header */
.site-header{position:absolute;left:0;top:0;width:1200px;height:86px;background:var(--white)}
.brand{left:148px;top:22px;display:flex;align-items:center;gap:10px}
.brand-mark{width:40px;height:40px;background:var(--blue)}
.brand-name{font-size:40px;font-weight:600;color:var(--blue);letter-spacing:-.5px}
.util{top:12px;font-size:13px;color:var(--blue);display:flex;align-items:center;gap:6px}
.util svg{width:16px;height:16px}
.util-sep{top:12px;width:1px;height:18px;background:#ddd}
.avatar{left:826px;top:5px;width:34px;height:34px;border-radius:50%;background:linear-gradient(#8a5a3c,#3a2418);border:2px solid var(--orange)}
.account-box{left:940px;top:11px;width:116px;height:22px;border:1px solid #bcd;display:flex;font-size:13px;color:var(--blue)}
.account-box span{display:flex;align-items:center;padding:0 4px}
.account-box span+span{border-left:1px solid #bcd;padding-left:7px}
.main-nav{top:54px;font-size:16px;color:var(--blue)}
.main-nav-sep{top:55px;width:1px;height:20px;background:#ddd}

/* category bar */
.category-bar{position:absolute;left:0;top:86px;width:1200px;height:44px;background:var(--bar)}
.cat{top:12px;font-size:16px;color:var(--white)}
.cat-sep{top:12px;width:1px;height:20px;background:#888}

/* hero */
.hero{position:absolute;left:0;top:130px;width:1200px;height:268px;background:linear-gradient(100deg,#f6f8fa 0%,var(--hero) 60%,#e6ebf1 100%)}
.select{left:251px;width:291px;height:34px;background:var(--white);border:1px solid var(--field-border);font-family:'Tinos',serif;font-size:13px;color:var(--blue-dark);display:flex;align-items:center;justify-content:space-between;padding:0 10px 0 8px}
.select svg{width:7px;height:11px}
.gender-field{left:248px;top:227px;width:209px;height:34px;background:var(--white);border:1px solid var(--field-border);font-family:'Roboto Condensed',sans-serif;font-size:13px;color:var(--blue-dark);display:flex;align-items:center;padding-left:10px}
.search-btn{left:457px;top:227px;width:88px;height:34px;background:var(--blue);color:var(--white);font-size:20px;display:flex;align-items:center;justify-content:center}
.hero-title{left:633px;top:62px;font-family:'Tinos',serif;font-size:25px;line-height:37px;color:var(--ink)}
.degree-icon{left:632px;top:153px;width:44px;height:44px;border-radius:50%;border:2px solid var(--orange);background:var(--white);display:flex;align-items:center;justify-content:center}
.degree-icon span{width:32px;height:32px;border-radius:50%;background:var(--blue)}
.degree-text{left:688px;top:162px;font-family:'Tinos',serif;font-size:18px;color:var(--ink)}

/* courses */
.section-title{left:0;top:416px;width:1200px;text-align:center;font-size:32px;color:var(--blue)}
.section-lead{left:0;top:460px;width:1200px;text-align:center;font-family:'Tinos',serif;font-size:14px}
.course-card{top:501px;width:214px;height:161px;background:var(--white);border:1px solid #e2e2e2;box-shadow:0 1px 3px rgba(0,0,0,.12);padding:5px}
.course-photo{position:relative;width:100%;height:100%;overflow:hidden}
.course-caption{position:absolute;left:0;bottom:0;width:100%;height:38px;background:rgba(40,40,40,.78);color:var(--white);font-size:13px;line-height:16px;padding:3px 4px}
.course-plus{position:absolute;right:0;bottom:0;width:0;height:0;border-left:28px solid transparent;border-bottom:38px solid var(--blue)}
.course-plus-sign{position:absolute;right:3px;bottom:3px;color:var(--white);font-size:18px;line-height:18px}
.dots{left:579px;top:679px;display:flex;gap:5px}
.dots span{width:7px;height:7px;background:var(--orange)}
.dots span:first-child{background:var(--blue)}

/* footer */
.site-footer{position:absolute;left:0;top:737px;width:1200px;height:236px;background:var(--footer);border-top:2px solid var(--blue)}
.foot-head{top:29px;font-size:15px;font-weight:500;color:var(--white)}
.foot-link{font-family:'Tinos',serif;font-size:15px;color:var(--white)}
.store-badge{left:441px;width:134px;height:47px;border:1px solid var(--blue);border-radius:4px;background:#000;color:var(--white);display:flex;align-items:center;justify-content:center;gap:8px;font-size:17px;font-weight:500}
.store-badge i{width:14px;height:14px;background:var(--white);display:block}
.social-dot{left:701px;width:31px;height:31px;border-radius:50%;background:var(--white);border:2px solid #ccc}
.social-dot.accent{border-color:var(--orange)}
.social-label{left:753px;font-family:'Tinos',serif;font-size:16px;color:var(--white)}
.foot-brand{left:906px;top:110px;display:flex;align-items:center;gap:8px}
.foot-brand i{width:24px;height:24px;background:#123d63;display:block}
.foot-brand span{font-size:30px;font-weight:600;color:#123d63}
.copyright{position:absolute;left:0;top:973px;width:1200px;height:28px;background:var(--copy-bar);color:var(--white);font-size:14px;text-align:center;line-height:28px}
</style>
</head>
<body>

<header class="site-header">
  <div class="abs brand"><span class="brand-mark"></span><span class="brand-name">K5Lesson</span></div>

  <div class="abs util" style="left:598px">
    <svg viewBox="0 0 16 16"><path d="M8 1 3 6h3v5h4V6h3z M1 12v3h14v-3h-2v1H3v-1z" fill="#333"/></svg>Sign Up</div>
  <div class="abs util-sep" style="left:682px"></div>
  <div class="abs util" style="left:692px">
    <svg viewBox="0 0 16 16"><circle cx="8" cy="8" r="6.5" fill="none" stroke="#333" stroke-width="2"/><path d="M6 8h6" stroke="#333" stroke-width="2"/></svg>Login</div>
  <div class="abs util-sep" style="left:760px"></div>
  <div class="abs util" style="left:774px">EN
    <svg viewBox="0 0 16 16" style="width:9px"><path d="M3 6l5 5 5-5" fill="none" stroke="#333" stroke-width="2"/></svg></div>
  <div class="abs util-sep" style="left:815px"></div>
  <div class="abs avatar" role="img" aria-label="User profile photo"></div>
  <div class="abs util" style="left:862px;top:14px">Hello User <span style="color:var(--orange);font-size:9px">&#9654;</span></div>
  <div class="abs account-box"><span>Menu <span style="color:var(--orange);font-size:9px;padding:0 0 0 4px">&#9660;</span></span><span>Sign Out</span></div>

  <div class="abs main-nav" style="left:640px">Home</div>
  <div class="abs main-nav-sep" style="left:707px"></div>
  <div class="abs main-nav" style="left:727px">Find A Tutor</div>
  <div class="abs main-nav-sep" style="left:837px"></div>
  <div class="abs main-nav" style="left:857px">About Us</div>
  <div class="abs main-nav-sep" style="left:948px"></div>
  <div class="abs main-nav" style="left:968px">Contact Us</div>
</header>

<nav class="category-bar">
  <div class="abs cat" style="left:144px">Academic</div>
  <div class="abs cat-sep" style="left:256px"></div>
  <div class="abs cat" style="left:284px">Music</div>
  <div class="abs cat-sep" style="left:360px"></div>
  <div class="abs cat" style="left:388px">I.T.</div>
  <div class="abs cat-sep" style="left:445px"></div>
  <div class="abs cat" style="left:473px">Languages</div>
  <div class="abs cat-sep" style="left:589px"></div>
  <div class="abs cat" style="left:617px">Business</div>
  <div class="abs cat-sep" style="left:713px"></div>
  <div class="abs cat" style="left:741px">Dance</div>
  <div class="abs cat-sep" style="left:822px"></div>
  <div class="abs cat" style="left:850px">Sports</div>
  <div class="abs cat-sep" style="left:925px"></div>
  <div class="abs cat" style="left:956px">Arts &amp; Crafts</div>
</nav>

<section class="hero">
  <div class="abs select" style="top:17px">Level 1<svg viewBox="0 0 7 11"><path d="M0 4.5 3.5 0 7 4.5zM0 6.5 3.5 11 7 6.5z" fill="var(--orange)"/></svg></div>
  <div class="abs select" style="top:60px">Level 2<svg viewBox="0 0 7 11"><path d="M0 4.5 3.5 0 7 4.5zM0 6.5 3.5 11 7 6.5z" fill="var(--orange)"/></svg></div>
  <div class="abs select" style="top:103px">Level 3<svg viewBox="0 0 7 11"><path d="M0 4.5 3.5 0 7 4.5zM0 6.5 3.5 11 7 6.5z" fill="var(--orange)"/></svg></div>
  <div class="abs select" style="top:144px">Level 4<svg viewBox="0 0 7 11"><path d="M0 4.5 3.5 0 7 4.5zM0 6.5 3.5 11 7 6.5z" fill="var(--orange)"/></svg></div>
  <div class="abs select" style="top:185px">Level 5<svg viewBox="0 0 7 11"><path d="M0 4.5 3.5 0 7 4.5zM0 6.5 3.5 11 7 6.5z" fill="var(--orange)"/></svg></div>
  <div class="abs gender-field">Male, Female, Both Selection</div>
  <div class="abs search-btn">Search</div>

  <h1 class="abs hero-title" style="font-weight:400">Preparing Students For<br>Successful Future</h1>
  <div class="abs degree-icon"><span></span></div>
  <div class="abs degree-text">Master &amp; PHD Degree Preparation</div>
</section>

<h2 class="abs section-title" style="font-weight:400">K5 Lesson Popular Courses</h2>
<p class="abs section-lead">Lorem ipsum dolor sit amet, consectetuer adipisc ing elit, sed diam nonummy nibh euismod tinunt ut laoreet.</p>

<div class="abs course-card" style="left:19px">
  <div class="course-photo" role="img" aria-label="Rolled diploma tied with a ribbon" style="background:linear-gradient(135deg,#efe3c0,#c9b88a)">
    <div class="course-caption">Advanced<br>Diploma Program</div><div class="course-plus"></div><div class="course-plus-sign">+</div></div>
</div>
<div class="abs course-card" style="left:256px">
  <div class="course-photo" role="img" aria-label="Instructor presenting to a business class" style="background:linear-gradient(180deg,#e8eef3,#7f95a8)">
    <div class="course-caption">Advanced Post Graduation<br>Business Management</div><div class="course-plus"></div><div class="course-plus-sign">+</div></div>
</div>
<div class="abs course-card" style="left:496px">
  <div class="course-photo" role="img" aria-label="Student desk with laptop, notes and markers" style="background:linear-gradient(135deg,#5a5a5a,#2e2e2e)">
    <div class="course-caption">American Curriculum<br>Grande 11 &amp; 12</div><div class="course-plus"></div><div class="course-plus-sign">+</div></div>
</div>
<div class="abs course-card" style="left:735px">
  <div class="course-photo" role="img" aria-label="Smiling student holding a green folder" style="background:linear-gradient(135deg,#8a8a8a,#c28b2a)">
    <div class="course-caption">Master in Business<br>Administration- Online MBA</div><div class="course-plus"></div><div class="course-plus-sign">+</div></div>
</div>
<div class="abs course-card" style="left:970px">
  <div class="course-photo" role="img" aria-label="Language test booklets with red pens" style="background:linear-gradient(135deg,#f2f2f2,#c8c8c8)">
    <div class="course-caption">LangTest<br>Coaching Programs</div><div class="course-plus"></div><div class="course-plus-sign">+</div></div>
</div>

<div class="abs dots"><span></span><span></span><span></span><span></span><span></span><span></span></div>

<footer class="site-footer">
  <div class="abs foot-head" style="left:143px">Quick Links</div>
  <div class="abs foot-head" style="left:442px">Download Our App From</div>
  <div class="abs foot-head" style="left:702px">Follow Us On</div>

  <div class="abs foot-link" style="left:146px;top:72px;line-height:25.6px">Home<br>Find A Tutor<br>About Us<br>Academic<br>Music<br>I.T.</div>
  <div class="abs foot-link" style="left:265px;top:72px;line-height:25.6px">Languages<br>Business<br>Dance<br>Sports<br>Arts &amp; Crafts<br>Contact Us</div>

  <div class="abs store-badge" style="top:71px"><i></i>Varnel Play</div>
  <div class="abs store-badge" style="top:135px;width:137px"><i></i>Orchard Apps</div>

  <div class="abs social-dot accent" style="top:70px"></div>
  <div class="abs social-label" style="top:76px">Friendly</div>
  <div class="abs social-dot" style="top:117px"></div>
  <div class="abs social-label" style="top:123px">Chirper</div>
  <div class="abs social-dot" style="top:165px"></div>
  <div class="abs social-label" style="top:172px">WorkLink</div>

  <div class="abs foot-brand"><i></i><span>K5Lesson</span></div>
</footer>
<div class="copyright">Copyright© 2016 &nbsp;K5Lesson . All Rights Reserved</div>

</body>
</html>
```